Consulting Company Business Card

I am looking for a minimalist, classy, professional design on my business card. I would like it to be double-sided. I want to use the font and color scheme of my logo which are attached. Please be creative in the designs that you send me. I want to play off the design of my logo with the inner C that is Green and Blue broken up with the white.
Target Market(s)
Small Businesses
Industry/Entity Type
Consulting
Contact Information for Business Card
Dale M. Whitcombe, CPA CGMA, 555-014-2873, dwhitcombe@vorantaadvisory.example, www.vorantaadvisory.example

```html
<!DOCTYPE html>
<html lang="en">
<head>
<meta charset="utf-8">
<title>Voranta Advisory Business Card</title>
<link rel="stylesheet" href="https://fonts.googleapis.com/css2?family=Poppins:wght@400;600;700&display=swap">
<style>
  :root {
    --backdrop: #e6e7ea;
    --paper: #eceef1;
    --navy: #1e2f54;
    --teal: #1f7a7a;
    --white: #f4f5f7;
  }
  * { margin: 0; padding: 0; box-sizing: border-box; }
  html, body {
    width: 1200px; height: 1200px; overflow: hidden;
    background: var(--backdrop);
    font-family: "Poppins", Arial, sans-serif;
  }
  .card {
    position: absolute; left: 227px; width: 746px; height: 426px;
    border-radius: 50px; overflow: hidden;
  }
  .card-front { top: 135px; background: var(--paper); }
  .card-back { top: 639px; background: var(--navy); }

  .brand-front {
    position: absolute; right: 38px; top: 38px; width: 220px;
    text-align: center; color: var(--navy); font-weight: 700;
  }
  .brand-dot {
    width: 72px; height: 72px; border-radius: 50%;
    background: var(--teal); margin: 0 auto 16px;
  }
  .brand-front .brand-name { font-size: 32px; line-height: 1; letter-spacing: 0.5px; }
  .brand-front .brand-sub { font-size: 13px; letter-spacing: 4.5px; margin-top: 6px; }

  .holder { position: absolute; left: 33px; top: 208px; }
  .holder-name { color: var(--teal); font-weight: 700; font-size: 25px; letter-spacing: 0.3px; line-height: 1.2; }
  .holder-title { color: var(--navy); font-size: 18px; line-height: 1.3; }

  .contact { position: absolute; left: 33px; top: 284px; color: var(--navy); font-size: 19px; }
  .contact-row { display: flex; align-items: center; gap: 8px; height: 27px; }
  .contact-icon { width: 19px; height: 19px; flex: none; }

  .band { position: absolute; left: 0; right: 0; top: 354px; height: 46px; }
  .band-navy { position: absolute; left: 0; top: 0; width: 410px; height: 46px; background: var(--navy); }
  .band-teal { position: absolute; left: 436px; right: 0; top: 0; height: 46px; background: var(--teal); }
  .band-dot {
    position: absolute; left: 398px; top: -1px; width: 48px; height: 48px;
    border-radius: 50%; background: var(--navy); border: 4px solid var(--paper);
  }
  .band-url {
    position: absolute; left: 436px; right: 0; top: 0; height: 46px;
    display: flex; align-items: center; justify-content: center;
    color: var(--white); font-size: 20px;
  }

  .brand-back {
    position: absolute; right: 48px; top: 160px; width: 356px;
    text-align: center; color: var(--white); font-weight: 700;
  }
  .brand-back .brand-name { font-size: 64px; line-height: 1; letter-spacing: 1px; }
  .brand-back .brand-sub { font-size: 24px; letter-spacing: 10px; margin-top: 10px; }
</style>
</head>
<body>
  <section class="card card-front">
    <div class="brand-front">
      <div class="brand-dot"></div>
      <div class="brand-name">VORANTA</div>
      <div class="brand-sub">ADVISORY</div>
    </div>

    <div class="holder">
      <div class="holder-name">DALE M. WHITCOMBE</div>
      <div class="holder-title">CPA CGMA</div>
    </div>

    <div class="contact">
      <div class="contact-row">
        <svg class="contact-icon" viewBox="0 0 20 20" aria-hidden="true">
          <circle cx="10" cy="10" r="10" fill="#1f7a7a"/>
          <path d="M7 5.5c-.8.4-1.4 1.3-1.2 2.4.6 3 3.3 5.7 6.3 6.3 1.1.2 2-.4 2.4-1.2l-1.8-1.6-1.3.8c-1.3-.6-2.4-1.7-3-3l.8-1.3z" fill="#f4f5f7"/>
        </svg>
        <span>555-014-2873</span>
      </div>
      <div class="contact-row">
        <svg class="contact-icon" viewBox="0 0 20 20" aria-hidden="true">
          <circle cx="10" cy="10" r="10" fill="#1f7a7a"/>
          <rect x="5" y="6.5" width="10" height="7" rx="1" fill="none" stroke="#f4f5f7" stroke-width="1.3"/>
          <path d="M5.4 7l4.6 3.6L14.6 7" fill="none" stroke="#f4f5f7" stroke-width="1.3"/>
        </svg>
        <span>dwhitcombe@vorantaadvisory.example</span>
      </div>
    </div>

    <div class="band">
      <div class="band-navy"></div>
      <div class="band-teal"></div>
      <div class="band-dot"></div>
      <div class="band-url">vorantaadvisory.example</div>
    </div>
  </section>

  <section class="card card-back">
    <div class="brand-back">
      <div class="brand-name">VORANTA</div>
      <div class="brand-sub">ADVISORY</div>
    </div>
  </section>
</body>
</html>
```